Glamour By Tavi

I am a makeup artist looking for professional looking double sided business card. I would like to create a logo and incorporate a set of eyes as the periods above the name "Tavi" on the card.

front of card: Logo "Glamour by Tavi" written across diagonal (bottom left to top right)

Back of card:
1) Professional makeup artist serving New York & New Jersey (or similar to this text)
2) 917-555-0148
3) glamourbytavi@mailcove.com

Industry/Entity Type

Business

```html
<!DOCTYPE html>
<html lang="en">
<head>
<meta charset="utf-8">
<title>Glamour by Tavi – Business Card</title>
<link rel="stylesheet" href="https://fonts.googleapis.com/css2?family=Poppins:wght@600;700&display=swap">
<style>
  :root {
    --page-bg: #ece9ee;
    --pink-deep: #c2307f;
    --pink-mid: #e05aa6;
    --sky: #b9d3ea;
    --sky-pale: #dbe9f6;
    --white: #ffffff;
    --plum: #7a1846;
  }
  * { box-sizing: border-box; margin: 0; padding: 0; }
  html, body {
    width: 1200px; height: 900px; overflow: hidden;
    background: var(--page-bg);
    font-family: "Poppins", sans-serif;
  }
  .canvas { position: relative; width: 1200px; height: 900px; }
  .card {
    position: absolute; width: 700px; height: 400px;
    border-radius: 22px; overflow: hidden;
    box-shadow: 0 10px 28px rgba(60, 30, 60, 0.18);
  }

  /* Front */
  .card-front {
    left: 60px; top: 40px;
    background: linear-gradient(135deg, var(--pink-mid), var(--pink-deep));
  }
  .front-band { position: absolute; inset: 0; }
  .front-art {
    position: absolute; left: 250px; top: 60px; width: 300px; height: 260px;
    transform: rotate(-24deg);
    background: radial-gradient(ellipse at center, rgba(255,255,255,0.55), rgba(255,255,255,0) 70%);
  }
  .brand-name {
    position: absolute; left: 0; top: 155px; width: 700px;
    text-align: center;
    font-size: 64px; font-weight: 700; line-height: 1;
    color: var(--pink-deep);
    transform: rotate(-24deg);
    transform-origin: 350px 35px;
  }

  /* Back */
  .card-back {
    left: 440px; top: 460px;
    background: linear-gradient(170deg, var(--white) 0%, var(--sky) 45%, var(--sky-pale) 75%, var(--white) 100%);
  }
  .tagline {
    position: absolute; left: 30px; top: 34px; width: 330px;
    text-align: center; color: var(--plum);
    font-size: 18px; font-weight: 600; line-height: 1.25;
  }
  .faces-art {
    position: absolute; left: 40px; top: 100px; width: 300px; height: 270px;
    border-radius: 14px;
    background: radial-gradient(ellipse at 50% 45%, rgba(255,255,255,0.7), rgba(185,211,234,0.2));
  }
  .divider {
    position: absolute; left: 372px; top: 70px; width: 2px; height: 250px;
    background: var(--plum);
  }
  .contact {
    position: absolute; left: 396px; top: 130px; width: 290px;
    color: var(--plum); font-size: 19px; font-weight: 600;
  }
  .contact .phone { display: block; padding-left: 56px; margin-bottom: 40px; }
  .contact .email { display: block; font-size: 17px; }
</style>
</head>
<body>
<main class="canvas">

  <section class="card card-front" aria-label="Card front">
    <svg class="front-band" width="700" height="400" viewBox="0 0 700 400" aria-hidden="true">
      <path d="M0 265 L700 -45 L700 125 L0 435 Z" fill="#dbe9f6"/>
      <path d="M0 265 L700 -45" fill="none" stroke="#ffffff" stroke-opacity="0.7" stroke-width="4"/>
      <path d="M0 435 L700 125" fill="none" stroke="#ffffff" stroke-opacity="0.7" stroke-width="4"/>
    </svg>
    <div class="front-art" role="img" aria-label="Illustrated makeup faces with bubbles and swirls"></div>
    <h1 class="brand-name">Glamour by Tavi</h1>
  </section>

  <section class="card card-back" aria-label="Card back">
    <p class="tagline">Professional makeup artist<br>serving New York &amp; New Jersey</p>
    <div class="faces-art" role="img" aria-label="Illustrated makeup faces with sparkles and bubbles"></div>
    <div class="divider"></div>
    <div class="contact">
      <span class="phone">917-555-0148</span>
      <span class="email">glamourbytavi@mailcove.com</span>
    </div>
  </section>

</main>
</body>
</html>
```